" UNFADING SPRINGTIDE 2020 ".

I want a flyer to invite people to a 2 Days Miracle Service. Salvation, Deliverance, Healing, Restoration, Breakthrough .
The best flyer you can propose me. Insert the logo i send you on the flyer. 04/11-04/12/2020. From 6:00Pm-10:00Pm. Venue: 5:00Pm. With Evangelist PAUL-HENRI MADOLEBA. ( LAMP & RIVER Ministry ) At: Tenbury Fellowship Hall. 24730 PELDRA Street, Romulus, Michigan 48174. Jesus-Christ Is the Lord.
Contact: - email : lampriverfel@outlook-mail.example
- cell phone: 5550419826
- Whatsapp :5550419826

Target Market(s)

Michigan, all ages

Font styles to use
Decorative
Script

Requirements
Must have
• Must have the logo of the ministry.

```html
<!DOCTYPE html>
<html lang="en">
<head>
<meta charset="utf-8">
<title>Unfading Springtide 2020 – 2 Days Miracle Service</title>
<link href="https://fonts.googleapis.com/css2?family=Cinzel:wght@600;700;800&family=Kaushan+Script&family=Abril+Fatface&family=Montserrat:wght@600;700;800&family=Lora:wght@700&display=swap" rel="stylesheet">
<style>
  :root{
    --night:#1d1a17;
    --gold-light:#f6dc8f;
    --gold:#e2b553;
    --gold-deep:#b8892f;
    --brown:#3b2414;
    --brown-mid:#5a3a1e;
    --white:#ffffff;
    --mist:#eceeec;
    --teal-dark:#2c3a36;
    --teal-mid:#4f625d;
    --ink:#2a1f18;
    --logo-red:#c8202a;
    --logo-blue:#1f5fb0;
  }
  html,body{margin:0;padding:0;overflow:hidden;background:var(--white);}
  .flyer{position:relative;width:927px;height:1200px;overflow:hidden;background:var(--mist);font-family:"Lora",serif;}
  .scene{position:absolute;left:0;top:0;width:927px;height:700px;
    background:
      radial-gradient(ellipse 170px 240px at 250px 300px,#fff3c9 0%,#f3b45a 35%,#b35a1e 62%,transparent 80%),
      radial-gradient(ellipse 420px 380px at 300px 280px,#5a4632 0%,#332a22 55%,transparent 85%),
      linear-gradient(180deg,#2a2520 0%,#1f2a22 45%,#2b3a2c 70%,#3a4a3e 100%);}
  .lower-backdrop{position:absolute;left:0;top:640px;width:927px;height:560px;
    background:linear-gradient(180deg,var(--teal-dark) 0%,#34453f 30%,var(--teal-mid) 42%,#c3ccc9 52%,#e4e8e6 64%,#f4f4f2 100%);}
  .speaker-photo{position:absolute;left:0;top:700px;width:370px;height:500px;
    background:linear-gradient(180deg,#4a3a36 0%,#3a2f30 55%,#8f8f8f 100%);
    border-radius:40% 50% 0 0 / 16% 20% 0 0;}
  .logo{position:absolute;left:728px;top:30px;width:170px;text-align:center;}
  .logo-disc{width:150px;height:150px;margin:0 auto;border-radius:50%;background:var(--logo-blue);}
  .logo-name{margin-top:8px;font-family:"Montserrat",sans-serif;font-weight:700;font-size:15px;color:var(--logo-red);}
  .title-top{position:absolute;left:0;width:670px;top:280px;text-align:center;font-family:"Cinzel",serif;font-weight:700;font-size:44px;color:var(--white);letter-spacing:1px;}
  .title-script{position:absolute;left:0;width:670px;top:345px;text-align:center;font-family:"Kaushan Script",cursive;font-size:110px;line-height:1.1;color:var(--gold);}
  .title-year{position:absolute;left:0;width:670px;top:475px;text-align:center;font-family:"Cinzel",serif;font-weight:700;font-size:48px;color:var(--white);letter-spacing:2px;}
  .gold-band{position:absolute;left:0;top:516px;width:927px;height:244px;}
  .big-two{position:absolute;left:160px;top:505px;font-family:"Abril Fatface",serif;font-size:250px;line-height:1;color:var(--brown);}
  .service-title{position:absolute;left:295px;top:580px;font-family:"Kaushan Script",cursive;font-size:58px;color:var(--brown);white-space:nowrap;}
  .themes{position:absolute;left:300px;width:600px;top:678px;text-align:center;font-family:"Cinzel",serif;font-weight:700;font-size:23px;line-height:30px;color:var(--brown-mid);}
  .with-line{position:absolute;left:405px;width:420px;top:768px;display:flex;align-items:center;gap:14px;font-family:"Montserrat",sans-serif;font-weight:600;font-size:21px;color:var(--white);}
  .with-line::before,.with-line::after{content:"";flex:1;height:2px;background:var(--white);}
  .evangelist{position:absolute;left:300px;width:630px;top:800px;text-align:center;font-family:"Montserrat",sans-serif;font-weight:800;font-size:36px;color:var(--white);letter-spacing:.5px;}
  .ministry{position:absolute;left:300px;width:630px;top:848px;text-align:center;font-family:"Montserrat",sans-serif;font-weight:700;font-size:21px;color:var(--white);}
  .details{position:absolute;left:370px;width:500px;top:896px;text-align:center;color:var(--ink);}
  .rule{height:2px;background:var(--brown-mid);margin:0 10px;}
  .dates{font-family:"Lora",serif;font-weight:700;font-size:26px;color:var(--brown-mid);margin:6px 0 2px;}
  .times{font-family:"Lora",serif;font-weight:700;font-size:24px;line-height:30px;color:var(--brown);}
  .contact{margin-top:14px;font-family:"Montserrat",sans-serif;font-weight:700;font-size:17px;line-height:23px;color:var(--ink);}
  .contact .rule{margin:8px 20px;}
  .address{font-family:"Montserrat",sans-serif;font-weight:700;font-size:18px;line-height:26px;color:var(--ink);}
  .closing{position:absolute;left:300px;width:630px;top:1140px;text-align:center;font-family:"Cinzel",serif;font-weight:700;font-size:28px;color:var(--brown);}
</style>
</head>
<body>
<main class="flyer">
  <div class="scene" role="img" aria-label="Photograph of an open rock tomb glowing with sunrise light, three crosses on a hill beyond, framed by greenery"></div>
  <div class="lower-backdrop" role="img" aria-label="Soft blurred blue-green light background with bokeh fading to pale grey"></div>

  <div class="logo">
    <div class="logo-disc"></div>
    <div class="logo-name">LAMP &amp; RIVER Ministries</div>
  </div>

  <div class="title-top">UNFADING</div>
  <div class="title-script">Springtide</div>
  <div class="title-year">2020</div>

  <svg class="gold-band" viewBox="0 0 927 244" aria-hidden="true">
    <defs>
      <linearGradient id="goldSheen" x1="0" y1="0" x2="1" y2="1">
        <stop offset="0" stop-color="#b8892f"/>
        <stop offset=".3" stop-color="#f6dc8f"/>
        <stop offset=".55" stop-color="#e2b553"/>
        <stop offset=".8" stop-color="#f3d68a"/>
        <stop offset="1" stop-color="#c4943a"/>
      </linearGradient>
    </defs>
    <path d="M0 16 C120 0 260 24 420 10 C600 -4 760 20 927 6 L927 222 C780 238 620 212 460 228 C300 244 150 218 0 234 Z" fill="url(#goldSheen)"/>
  </svg>

  <div class="speaker-photo" role="img" aria-label="Photo of the evangelist in a dark blazer and red shirt, one hand raised, singing into a microphone"></div>

  <div class="big-two">2</div>
  <div class="service-title">Days Miracle Service</div>
  <div class="themes">Salvation, Deliverance, Healing,<br>Restoration, Breakthrough</div>

  <div class="with-line">With Evangelist</div>
  <div class="evangelist">PAUL-HENRI MADOLEBA</div>
  <div class="ministry">LAMP &amp; RIVER Ministry</div>

  <section class="details">
    <div class="rule"></div>
    <div class="dates">April 11, 2020 &nbsp;|&nbsp; April 12, 2020</div>
    <div class="times">6:00PM-10:00PM<br>Venue: 5:00PM</div>
    <div class="contact">
      email : lampriverfel@outlook-mail.example<br>
      Mobile: 5550419826 | Whatsapp :5550419826
      <div class="rule"></div>
    </div>
    <div class="address">Tenbury Fellowship Hall &nbsp;|&nbsp; 24730 PELDRA Street<br>| Romulus | Michigan 48174</div>
  </section>

  <div class="closing">Jesus-Christ Is the Lord.</div>
</main>
</body>
</html>
```